Criação de Papelaria Profissional para Contabilidade & Finanças
" ESTOU INICANDO AGORA O ESCRITORIO DE CONTABILIDADE, QUERO ATUAR NO RAMO DE TREINAMENTO ATRAVÉS DO COACHING , FAZER CONSULTORIAS NA AREA CONTABIL, SERVIÇOS CONTABEIS EM GERAL, DESDE O MICROEMPREENDEDOR ATÉ O A EMPRESA DE GRANDE PORTE LUCRO REAL "

```html
<!DOCTYPE html>
<html lang="pt-BR">
<head>
<meta charset="utf-8">
<title>Vértice — Papel Timbrado</title>
<link rel="stylesheet" href="https://fonts.googleapis.com/css2?family=Montserrat:wght@400;500;700;800&display=swap">
<style>
  :root {
    --backdrop: #e6e4e1;
    --paper: #ffffff;
    --navy: #12133f;
    --gold: #d9a21b;
    --ink: #1d1d24;
    --muted: #6d6d74;
    --ghost: #e8e8e8;
  }
  * { margin: 0; padding: 0; box-sizing: border-box; }
  html, body {
    width: 1200px; height: 1200px; overflow: hidden;
    background: var(--backdrop);
    font-family: "Montserrat", sans-serif;
  }
  .canvas {
    width: 1200px; height: 1200px;
    display: flex; align-items: center; justify-content: center;
  }
  .letterhead {
    position: relative;
    width: 792px; height: 1120px;
    background: var(--paper);
    box-shadow: 0 10px 30px rgba(0,0,0,.12);
    overflow: hidden;
  }
  .edge-mark {
    position: absolute; top: 30px;
    width: 14px; height: 100px;
    background: var(--navy);
  }
  .edge-mark--left { left: 0; }
  .edge-mark--right { right: 0; }
  .brand {
    position: absolute; top: 52px; left: 0; right: 0;
    display: flex; align-items: center; justify-content: center; gap: 14px;
  }
  .brand__square {
    width: 30px; height: 30px; background: var(--navy);
  }
  .brand__name {
    font-weight: 800; font-size: 54px; letter-spacing: 1px;
    color: var(--navy);
  }
  .watermark {
    position: absolute; top: 250px; left: 0; right: 0;
    height: 720px;
    display: flex; align-items: center; justify-content: center;
  }
  .watermark__name {
    font-weight: 800; font-size: 150px; color: var(--ghost);
    transform: rotate(-90deg); white-space: nowrap;
  }
  .contact-bar {
    position: absolute; left: 0; right: 0; bottom: 32px;
    display: flex; justify-content: center; align-items: center; gap: 38px;
    font-size: 11px; color: var(--muted);
  }
  .contact-bar__item { display: flex; align-items: center; gap: 9px; line-height: 1.35; }
  .contact-bar__icon { width: 18px; height: 18px; flex: none; }
  .footer-band {
    position: absolute; left: 0; right: 0; bottom: 0;
    height: 12px; background: var(--navy);
  }
</style>
</head>
<body>
<main class="canvas">
  <article class="letterhead">
    <span class="edge-mark edge-mark--left"></span>
    <span class="edge-mark edge-mark--right"></span>

    <header class="brand">
      <span class="brand__square"></span>
      <span class="brand__name">Vértice</span>
    </header>

    <div class="watermark" aria-hidden="true">
      <span class="watermark__name">Vértice</span>
    </div>

    <footer class="contact-bar">
      <div class="contact-bar__item">
        <svg class="contact-bar__icon" viewBox="0 0 24 24" fill="none" stroke="var(--gold)" stroke-width="2" stroke-linecap="round" stroke-linejoin="round">
          <path d="M5 3h4l2 5-3 2a12 12 0 0 0 6 6l2-3 5 2v4a2 2 0 0 1-2 2A17 17 0 0 1 3 5a2 2 0 0 1 2-2z"/>
        </svg>
        <span>00 0000-0000 | 00 00000-0000</span>
      </div>
      <div class="contact-bar__item">
        <svg class="contact-bar__icon" viewBox="0 0 24 24" fill="none" stroke="var(--gold)" stroke-width="2" stroke-linejoin="round">
          <rect x="3" y="5" width="18" height="14" rx="1"/>
          <path d="M3 6l9 7 9-7"/>
        </svg>
        <span>seuemail@seuemail.com.br</span>
      </div>
      <div class="contact-bar__item">
        <svg class="contact-bar__icon" viewBox="0 0 24 24" fill="none" stroke="var(--gold)" stroke-width="2">
          <path d="M12 22s7-7 7-12a7 7 0 0 0-14 0c0 5 7 12 7 12z"/>
          <circle cx="12" cy="10" r="2.5"/>
        </svg>
        <span>Nome da Rua, 00 - Bairro<br>Cidade - Estado e CEP</span>
      </div>
      <div class="contact-bar__item">
        <svg class="contact-bar__icon" viewBox="0 0 24 24" fill="none" stroke="var(--gold)" stroke-width="2">
          <circle cx="12" cy="12" r="9"/>
        </svg>
        <span>verticecontabil</span>
      </div>
    </footer>

    <span class="footer-band"></span>
  </article>
</main>
</body>
</html>
```